Flyer redesign

We need this flier {Seasonal Care back 2018} redesigned for our 2019 season. It is attached below. New design should look different from current design. Be creative yet still professional.

Requirements
Must have
• Designed in photoshop.
• Should have the same text as current design. Only is "2019" instead of 2018. We want a different look with same info to send our customers next year.
• size: standard letter paper 8.5" x 11"
Nice to have
• Can use optional images provided. Not required though. See our website for more photos. thornbrookmemorial.org. send message through briskdrafts if you want a specific photo.
Should not have
• Do not take current design and just change date or image. Make the design look different.

```html
<!DOCTYPE html>
<html lang="en">
<head>
<meta charset="utf-8">
<title>Thornbrook Memorial – 2019 Gravesite Landscaping Packages</title>
<link href="https://fonts.googleapis.com/css2?family=Cabin:wght@400;500&family=Libre+Baskerville:wght@400;700&family=Montserrat:wght@800&family=Oswald:wght@500&display=swap" rel="stylesheet">
<style>
  :root {
    --wine: #6e1420;
    --wine-text: #7a1a28;
    --steel: #97adc2;
    --gold: #e0aa1e;
    --ink: #1d1d1d;
    --paper: #ffffff;
  }
  * { box-sizing: border-box; margin: 0; padding: 0; }
  html, body { width: 848px; height: 1200px; overflow: hidden; background: var(--paper); }
  .flyer { position: relative; width: 848px; height: 1200px; background: var(--paper); font-family: "Cabin", sans-serif; color: var(--ink); }

  .brand { position: absolute; top: 72px; left: 0; width: 100%; text-align: center;
    font-family: "Cabin", sans-serif; font-size: 34px; font-weight: 500; color: var(--wine-text); letter-spacing: 4px; }

  .hero { position: absolute; top: 155px; left: 0; width: 848px; height: 540px;
    background: linear-gradient(180deg, #b9c89a 0%, #a8925a 30%, #8a3a28 48%, #6f8a4a 68%, #7d9a52 85%, #8a8f88 100%); }
  .arch { position: absolute; top: 155px; left: 0; width: 848px; height: 172px; }
  .title { position: absolute; top: 164px; left: 0; width: 100%; text-align: center; font-family: "Cabin", sans-serif; font-weight: 400;
    font-size: 33px; line-height: 43px; letter-spacing: 7px; color: var(--ink); }

  .band { position: absolute; top: 694px; left: 0; width: 848px; height: 428px; background: var(--steel); }
  .footer { position: absolute; top: 1122px; left: 0; width: 848px; height: 78px; background: var(--wine); }
  .contacts { position: absolute; top: 1168px; left: 0; width: 100%; display: flex; justify-content: space-around; color: #fff;
    font-size: 16px; letter-spacing: 0.6px; padding: 0 38px; }
  .contacts span { width: 240px; text-align: center; }

  .card { position: absolute; top: 628px; width: 240px; height: 530px; background: var(--paper); border-radius: 32px; overflow: hidden; }
  .card--seasonal { left: 46px; }
  .card--basic { left: 304px; }
  .card--perpetual { left: 562px; }
  .card-head { background: var(--wine); height: 96px; color: #fff; text-align: center; padding-top: 4px; }
  .card-name { font-family: "Montserrat", sans-serif; font-weight: 800; font-size: 19px; letter-spacing: 3px; line-height: 24px; }
  .card-tag { font-size: 13px; line-height: 17px; margin-top: 1px; letter-spacing: 0.3px; }
  .features { list-style: none; padding: 13px 28px 0 21px; }
  .features li { position: relative; padding-left: 17px; font-size: 12.5px; line-height: 17px; letter-spacing: 0.7px; margin-bottom: 17px; }
  .features li svg { position: absolute; left: 0; top: 2px; }

  .badge { position: absolute; top: 602px; left: 596px; width: 170px; height: 26px; background: var(--gold); border-radius: 13px 13px 0 0;
    font-family: "Oswald", sans-serif; font-weight: 500; font-size: 19px; letter-spacing: 1.5px; text-align: center; line-height: 28px; color: var(--ink); }

  .price-stack { position: absolute; left: 0; width: 100%; text-align: center; font-family: "Libre Baskerville", serif; font-weight: 700; }
  .term { font-size: 19px; line-height: 20px; color: var(--ink); }
  .term--pay { line-height: 25px; }
  .amount { font-size: 36px; line-height: 40px; color: var(--wine-text); margin-bottom: 10px; }
  .amount--big { font-size: 38px; }
  .note { position: absolute; left: 0; width: 100%; text-align: center; font-size: 12px; line-height: 15px; letter-spacing: 0.3px; }
  .note--fine { font-size: 8.5px; line-height: 12px; letter-spacing: 0; }
</style>
</head>
<body>
<div class="flyer">
  <header class="brand">Thornbrook Memorial</header>

  <div class="hero" role="img" aria-label="Photo of the cemetery grounds in autumn: a red maple, rows of headstones on green lawn and a curving road under tall trees"></div>
  <svg class="arch" viewBox="0 0 848 172" preserveAspectRatio="none" aria-hidden="true">
    <path d="M80 0 C130 110 270 170 424 170 C578 170 718 110 768 0 Z" fill="#ffffff"/>
  </svg>
  <h1 class="title">2019<br>Gravesite Landscaping<br>Packcages</h1>

  <div class="band"></div>
  <footer class="footer"></footer>
  <div class="contacts"><span>info@thornbrookmemorial.org</span><span>(201) 555-0148</span><span>www.thornbrookmemorial.org</span></div>

  <section class="card card--seasonal">
    <div class="card-head">
      <h2 class="card-name">SEASONAL<br>CARE</h2>
      <p class="card-tag">Seasonal landscaping<br>grave care.</p>
    </div>
    <ul class="features">
      <li><svg width="12" height="11" viewBox="0 0 12 11"><path d="M1 6 L4.5 9.5 L11 1" fill="none" stroke="#7a1a28" stroke-width="2.4"/></svg>Weeding and trimming services on your gravesite approximately every 7 weeks during the growing season; mid-April through mid-October.</li>
    </ul>
    <div class="price-stack" style="top:280px">
      <div class="term">3 YEARS</div><div class="amount">$327</div>
      <div class="term">2 YEARS</div><div class="amount">$218</div>
      <div class="term">1 YEAR</div><div class="amount">$109</div>
    </div>
    <p class="note" style="top:497px">Multi-year payment<br>locks in current rates</p>
  </section>

  <section class="card card--basic">
    <div class="card-head">
      <h2 class="card-name">BASIC CARE<br>ENDOWMENT</h2>
      <p class="card-tag">Landscaping care forever for<br>graves whith no plantes</p>
    </div>
    <ul class="features">
      <li><svg width="12" height="11" viewBox="0 0 12 11"><path d="M1 6 L4.5 9.5 L11 1" fill="none" stroke="#7a1a28" stroke-width="2.4"/></svg>Weeding and trimming services on your gravesite 2 times per year: mid-May and mid-September.</li>
      <li><svg width="12" height="11" viewBox="0 0 12 11"><path d="M1 6 L4.5 9.5 L11 1" fill="none" stroke="#7a1a28" stroke-width="2.4"/></svg>Monument leveling.</li>
      <li><svg width="12" height="11" viewBox="0 0 12 11"><path d="M1 6 L4.5 9.5 L11 1" fill="none" stroke="#7a1a28" stroke-width="2.4"/></svg>Payment ensures grave care forever.</li>
    </ul>
    <div class="price-stack" style="top:390px">
      <div class="term term--pay">12 MONTHLY<br>PAYMENTS OF</div><div class="amount amount--big">$225.00*</div>
    </div>
    <p class="note note--fine" style="top:492px">*gravesites whith single headstones.<br>Call for other monument types and single<br>payment discount. Valid through 10/31/19.</p>
  </section>

  <div class="badge">MOST POPULAR</div>
  <section class="card card--perpetual">
    <div class="card-head">
      <h2 class="card-name">PERPETUALCARE<br>ENDOWMENT</h2>
      <p class="card-tag">Landscaping care forever for<br>graves whith plantes</p>
    </div>
    <ul class="features">
      <li><svg width="12" height="11" viewBox="0 0 12 11"><path d="M1 6 L4.5 9.5 L11 1" fill="none" stroke="#7a1a28" stroke-width="2.4"/></svg>Weeding and trimming services on your gravesite approximately every 7 weeks during the growing season; mid-April through mid-October.</li>
      <li><svg width="12" height="11" viewBox="0 0 12 11"><path d="M1 6 L4.5 9.5 L11 1" fill="none" stroke="#7a1a28" stroke-width="2.4"/></svg>Monument leveling and cleaning.</li>
      <li><svg width="12" height="11" viewBox="0 0 12 11"><path d="M1 6 L4.5 9.5 L11 1" fill="none" stroke="#7a1a28" stroke-width="2.4"/></svg>Payment ensures grave care forever.</li>
      <li><svg width="12" height="11" viewBox="0 0 12 11"><path d="M1 6 L4.5 9.5 L11 1" fill="none" stroke="#7a1a28" stroke-width="2.4"/></svg>Full bed of boxwood shrubs.</li>
      <li><svg width="12" height="11" viewBox="0 0 12 11"><path d="M1 6 L4.5 9.5 L11 1" fill="none" stroke="#7a1a28" stroke-width="2.4"/></svg>Trust certificate.</li>
    </ul>
    <div class="price-stack" style="top:390px">
      <div class="term term--pay">12 MONTHLY<br>PAYMENTS OF</div><div class="amount amount--big">$280.42</div>
    </div>
    <p class="note" style="top:492px">Call for single payment discount.<br>Valid through 10/31/19</p>
  </section>
</div>
</body>
</html>
```